Home care support

Design a a great and dynamic website for a healthcare business. Our business will be involved in providing care at home for people with disability and the elderly. Below is a link that I found for a company offering similar services in the US. I am looking for something like this .
I have my files - the latest project in here in through through PixelNest
Sample site : https://pinegroveattendants.net/
Target Market(s)
people with disability and elderly seniors who need home care support
Industry/Entity Type
Health
Coding
Coded - Design and coding required
Number of Pages Required
5+ page
Requirements
Must have
- inspirational pictures and designed with the themed logo (files attached)
Nice to have
- This is my sample and should look like this : https://pinegroveattendants.net/

```html
<!DOCTYPE html>
<html lang="en">
<head>
<meta charset="utf-8">
<title>Marlow Health Care – Home Care Support</title>
<link href="https://fonts.googleapis.com/css2?family=Montserrat:wght@400;500;600;700&family=Noto+Serif:wght@400&display=swap" rel="stylesheet">
<style>
:root{
  --blue:#1b6fa3;
  --blue-dark:#0f5f8e;
  --green:#5b9b3f;
  --ink:#1c1c1c;
  --grey:#6b6b6b;
  --ice:#e3eff4;
  --ice-circle:#d2e4ec;
  --white:#ffffff;
}
*{box-sizing:border-box;margin:0;padding:0}
html,body{width:1200px;height:4906px;overflow:hidden}
body{position:relative;background:var(--white);font-family:"Montserrat",sans-serif;color:var(--ink)}
.abs{position:absolute}
.serif{font-family:"Noto Serif",serif}

/* header */
.topbar{left:0;top:0;width:1200px;height:53px;background:var(--blue)}
.topbar .socials{left:482px;top:17px;display:flex;gap:10px}
.topbar .socials span{width:14px;height:14px;border-radius:50%;background:var(--white);opacity:.9;display:block}
.topbar .call{left:630px;top:18px;color:var(--white);font-size:14px;display:flex;align-items:center;gap:8px}
.topbar .appt{left:825px;top:0;width:225px;height:53px;background:var(--green);color:var(--white);font-size:14px;font-weight:600;display:flex;align-items:center;justify-content:center}
.brand{left:86px;top:10px;width:170px;text-align:center}
.brand .mark{width:84px;height:84px;border-radius:50%;background:var(--white);border:4px solid var(--blue);margin:0 auto}
.brand .name{font-size:30px;font-weight:700;color:var(--blue);letter-spacing:1px;margin-top:4px}
.nav{left:306px;top:92px;display:flex;font-size:16px;font-weight:500}
.nav a{color:var(--ink);text-decoration:none;position:absolute;white-space:nowrap}
.nav a.active{color:var(--blue)}

/* hero */
.hero-photo{left:0;top:141px;width:1200px;height:640px;background:linear-gradient(100deg,#b89a86 0%,#e9ddd3 35%,#f2ece6 60%,#d9d2cc 100%)}
.hero-badge{left:680px;top:214px;width:384px;height:384px;border-radius:50%;background:var(--green)}
.hero-badge .inner{position:absolute;left:0;top:0;width:372px;height:372px;border-radius:50%;background:var(--blue);border:6px solid var(--white);display:flex;flex-direction:column;align-items:center;justify-content:center;color:var(--white)}
.hero-badge h1{font-size:58px;font-weight:600;line-height:1;letter-spacing:1px}
.hero-badge h2{font-size:34px;font-weight:500;margin-top:6px}
.btn{background:linear-gradient(90deg,var(--blue-dark),var(--green));color:var(--white);font-weight:600;font-size:15px;border-radius:26px;display:flex;align-items:center;justify-content:center;box-shadow:0 3px 6px rgba(0,0,0,.2)}
.hero-badge .btn{margin-top:24px;width:238px;height:46px;background:var(--green);font-size:13px}

/* about */
.section-title{font-size:40px;font-weight:600;line-height:1.25;color:var(--ink)}
.section-title .b{color:var(--blue)}
.section-title .g{color:var(--green)}
.underline{height:4px;width:133px;background:var(--green)}
.about-text{left:585px;top:918px;width:500px;font-size:17px;line-height:1.42;color:var(--ink)}
.about-mark{left:72px;top:1095px;width:480px;height:444px;border-radius:50%;background:radial-gradient(circle at 40% 40%,#d6c7b8,#9b8775 70%,#6f5c4c)}
.feature{width:220px}
.feature .icon{position:absolute;left:0;top:0}
.feature h3{position:absolute;left:56px;top:0;font-size:15px;font-weight:500;white-space:nowrap}
.feature p{position:absolute;left:56px;top:24px;width:190px;font-size:12px;line-height:1.35;color:var(--grey)}

/* committed */
.commit-bg{left:0;top:1619px;width:1200px;height:620px;background:linear-gradient(90deg,#f4f4f4 0%,#e6e6e6 40%)}
.commit-photo{left:571px;top:1619px;width:629px;height:620px;background:linear-gradient(90deg,#d9d1c8,#c7b4a2 40%,#2a62a8 80%,#1f4f96)}
.commit-title{left:145px;top:1794px;font-size:32px;font-weight:500;line-height:1.28}
.commit-text{left:145px;top:1890px;width:395px;font-size:18px;line-height:1.36}
.commit-btn{left:145px;top:2027px;width:176px;height:50px}

/* services */
.services-bg{left:0;top:2134px;width:1200px;height:1124px;background:var(--ice)}
.services-title{left:0;top:2340px;width:1200px;text-align:center}
.service{width:304px;height:304px;border-radius:50%;background:var(--ice-circle);text-align:center}
.service svg{position:absolute;left:112px;top:34px}
.service h3{position:absolute;left:0;top:138px;width:100%;font-size:17px;font-weight:500}
.service p{position:absolute;left:50px;top:176px;width:204px;font-size:11.5px;line-height:1.5;color:var(--grey)}
.services-btn{left:480px;top:3110px;width:238px;height:50px}

/* blog */
.blog-card .thumb{position:absolute;width:240px;height:210px;border-radius:24px 0 24px 0}
.blog-card h3{position:absolute;font-size:16px;font-weight:600;line-height:1.2;width:170px}
.blog-card p{position:absolute;font-size:12px;line-height:1.4;color:var(--grey);width:170px}
.blog-card .date{position:absolute;font-size:12px;font-weight:700;color:var(--blue)}

/* contact */
.contact-bg{left:0;top:3791px;width:1200px;height:781px;background:linear-gradient(90deg,#0f6b8e 0%,#2c7a7c 45%,#5a9a48 100%)}
.contact-title{left:0;top:3868px;width:1200px;text-align:center;color:var(--white);font-size:40px;font-weight:500}
.contact-sub{left:0;top:3936px;width:1200px;text-align:center;color:var(--white);font-size:29px}
.c-item{display:flex;align-items:center;gap:14px;color:var(--white);font-size:14px;line-height:1.3}
.c-item .dot{width:42px;height:42px;border-radius:50%;background:var(--white);display:flex;align-items:center;justify-content:center}
.field{background:var(--white);border-radius:4px;font-size:14px;color:var(--ink);padding:18px 18px}
.submit{left:528px;top:4360px;width:144px;height:46px;font-size:15px}

/* footer */
.footer-brand{left:149px;top:4606px;width:181px;text-align:center}
.footer-brand .mark{width:90px;height:90px;border-radius:50%;border:4px solid var(--blue);margin:0 auto}
.footer-brand .name{font-size:36px;font-weight:700;color:var(--blue);margin-top:2px}
.f-head{font-size:16px;font-weight:500;color:#333;letter-spacing:.5px}
.f-text{font-size:12px;line-height:1.4;color:#444}
.f-links{font-size:12px;line-height:1.85;color:#444}
.social{width:48px;height:48px;border-radius:50%;border:2px solid var(--blue)}
.f-input{left:808px;top:4705px;width:242px;height:38px;border:1px solid #ddd;border-radius:19px;font-size:12px;padding:11px 16px;color:#555;font-family:"Noto Serif",serif}
.f-submit{left:808px;top:4755px;width:242px;height:44px}
.divider{left:110px;top:4839px;width:980px;height:1px;background:#ddd}
.copyright{left:0;top:4866px;width:1200px;text-align:center;font-size:12px;color:#333}
</style>
</head>
<body>

<!-- header -->
<div class="abs topbar">
  <div class="abs socials"><span></span><span></span><span></span><span></span></div>
  <div class="abs call">
    <svg width="14" height="14" viewBox="0 0 24 24"><path d="M6.6 10.8a15 15 0 0 0 6.6 6.6l2.2-2.2c.3-.3.7-.4 1-.2 1.1.4 2.3.6 3.6.6.6 0 1 .4 1 1V20c0 .6-.4 1-1 1A17 17 0 0 1 3 4c0-.6.4-1 1-1h3.5c.6 0 1 .4 1 1 0 1.3.2 2.5.6 3.6.1.3 0 .7-.2 1z" fill="#fff"/></svg>
    Call Us: 555 214 0387
  </div>
  <div class="abs appt">MAKE AN APPOINTMENT</div>
</div>
<div class="abs brand">
  <div class="mark"></div>
  <div class="name">MARLOW</div>
</div>
<nav class="abs nav">
  <a class="active" style="left:0">Home</a>
  <a style="left:99px">About</a>
  <a style="left:198px">Services</a>
  <a style="left:314px">FAQ</a>
  <a style="left:398px">Resources</a>
  <a style="left:530px">Employment</a>
  <a style="left:684px">Contact</a>
</nav>

<!-- hero -->
<div class="abs hero-photo" role="img" aria-label="Photo of a smiling caregiver with her hand on the shoulder of an elderly woman seated at home"></div>
<div class="abs hero-badge">
  <div class="inner">
    <h1>MARLOW</h1>
    <h2>HEALTH CARE</h2>
    <div class="btn">MAKE AN APPOINTMENT</div>
  </div>
</div>
<svg class="abs" style="left:0;top:700px" width="1200" height="110" viewBox="0 0 1200 110">
  <path d="M0 40 Q600 150 1200 20 L1200 110 L0 110 Z" fill="#fff"/>
  <path d="M40 48 Q600 140 1200 22 Q600 120 40 48Z" fill="var(--blue)"/>
</svg>

<!-- about -->
<h2 class="abs section-title" style="left:149px;top:906px">ABOUT <span class="b">MARLOW</span><br><span class="g">HEALTH CARE</span></h2>
<div class="abs underline" style="left:149px;top:1034px"></div>
<p class="abs about-text serif">Lorem ipsum dolor sit amet, consectetur adipiscinglit, sed do eiusmod tempor incididunt ut labore et dolore magna aliqua. Quis ipsum sumod tempor incididunt ut labore et dolore agna aliqua.</p>
<div class="abs about-mark" role="img" aria-label="Large circular emblem filled with a photo of elderly people with their caregivers"></div>

<div class="abs feature" style="left:588px;top:1130px">
  <svg class="icon" width="44" height="34" viewBox="0 0 44 34"><circle cx="10" cy="8" r="5" fill="var(--blue)"/><circle cx="22" cy="6" r="6" fill="var(--green)"/><circle cx="34" cy="8" r="5" fill="var(--blue)"/><path d="M2 26a8 8 0 0 1 16 0zM12 26a10 10 0 0 1 20 0zM26 26a8 8 0 0 1 16 0z" fill="var(--blue)"/></svg>
  <h3>Friendly Staff</h3>
  <p class="serif">Lorem ipsum dolor sit amet con sectetur adipiscinglited do eiusmod tempor</p>
</div>
<div class="abs feature" style="left:858px;top:1130px">
  <svg class="icon" width="36" height="36" viewBox="0 0 24 24"><path d="M6.6 10.8a15 15 0 0 0 6.6 6.6l2.2-2.2c.3-.3.7-.4 1-.2 1.1.4 2.3.6 3.6.6.6 0 1 .4 1 1V20c0 .6-.4 1-1 1A17 17 0 0 1 3 4c0-.6.4-1 1-1h3.5c.6 0 1 .4 1 1 0 1.3.2 2.5.6 3.6.1.3 0 .7-.2 1z" fill="var(--blue)"/></svg>
  <h3>On Call 24/7</h3>
  <p class="serif">Lorem ipsum dolor sit amet con sectetur adipiscinglited do eiusmod tempor</p>
</div>
<div class="abs feature" style="left:588px;top:1256px">
  <svg class="icon" width="34" height="38" viewBox="0 0 34 38"><circle cx="17" cy="10" r="8" fill="var(--blue)"/><path d="M3 36a14 14 0 0 1 28 0z" fill="var(--blue)"/></svg>
  <h3>Choice of Caregiver</h3>
  <p class="serif">Lorem ipsum dolor sit amet con sectetur adipiscinglited do eiusmod tempor</p>
</div>
<div class="abs feature" style="left:858px;top:1252px">
  <svg class="icon" width="34" height="36" viewBox="0 0 34 36"><rect x="2" y="6" width="30" height="28" rx="3" fill="var(--blue)"/><rect x="8" y="1" width="4" height="9" fill="var(--blue)"/><rect x="22" y="1" width="4" height="9" fill="var(--blue)"/><rect x="6" y="14" width="22" height="2" fill="#fff"/></svg>
  <h3>Flexible Schedule</h3>
  <p class="serif">Lorem ipsum dolor sit amet con sectetur adipiscinglited do eiusmod tempor</p>
</div>
<div class="abs feature" style="left:588px;top:1386px">
  <svg class="icon" width="40" height="34" viewBox="0 0 40 34"><path d="M20 4c6 6 6 16 0 24-6-8-6-18 0-24z" fill="var(--green)"/><path d="M2 14c10 0 18 6 18 16C10 30 2 24 2 14zM38 14c-10 0-18 6-18 16 10 0 18-6 18-16z" fill="var(--blue)"/></svg>
  <h3>Peace of Mind</h3>
  <p class="serif">Lorem ipsum dolor sit amet con sectetur adipiscinglited do eiusmod tempor</p>
</div>
<div class="abs feature" style="left:858px;top:1386px">
  <svg class="icon" width="38" height="36" viewBox="0 0 38 36"><path d="M4 12h8l18-9v30L12 24H4z" fill="var(--blue)"/><rect x="8" y="24" width="6" height="10" fill="var(--blue)"/></svg>
  <h3>Free Assessments</h3>
  <p class="serif">Lorem ipsum dolor sit amet con sectetur adipiscinglited do eiusmod tempor</p>
</div>

<!-- committed -->
<div class="abs commit-bg"></div>
<div class="abs commit-photo" role="img" aria-label="Photo of a smiling senior woman holding hands with a nurse in a blue uniform"></div>
<svg class="abs" style="left:0;top:1600px" width="1200" height="60" viewBox="0 0 1200 60">
  <path d="M0 0H1200V10Q700 0 180 60H0Z" fill="#fff"/>
  <path d="M220 42 Q700 -6 1200 16 Q700 4 220 42Z" fill="var(--blue)"/>
</svg>
<svg class="abs" style="left:0;top:2120px" width="1200" height="120" viewBox="0 0 1200 120">
  <path d="M0 20 Q600 130 1200 10 V120 H0Z" fill="var(--ice)"/>
  <path d="M240 70 Q700 120 1120 64 Q700 108 240 70Z" fill="var(--blue)"/>
</svg>
<h2 class="abs commit-title">We are Committed to<br>Your Well Being</h2>
<p class="abs commit-text serif">Lorem ipsum dolor sit amet, consectetur adi piscing elit, sed do eiusmod tempor incididu nt ut labore et dolore magna aliqua. Quis ips um suspendisse ultrices gravida.</p>
<div class="abs btn commit-btn">READ MORE</div>

<!-- services -->
<div class="abs services-bg" style="top:2236px;height:1022px"></div>
<h2 class="abs section-title services-title">OUR <span class="b">SERVICES</span></h2>
<div class="abs underline" style="left:533px;top:2394px;width:134px"></div>

<div class="abs service" style="left:130px;top:2441px">
  <svg width="80" height="90" viewBox="0 0 80 90" fill="none" stroke="var(--blue)" stroke-width="2.5"><path d="M40 44C22 30 22 16 32 14c4 0 6 2 8 6 2-4 4-6 8-6 10 2 10 16-8 30z" stroke="var(--green)"/><path d="M6 62h14l16 6h18c4 0 4 6 0 6H38M20 82l18 4 34-14c4-2 2-8-2-6L52 72"/><rect x="2" y="58" width="10" height="28"/></svg>
  <h3>Companion Care</h3>
  <p class="serif">Lorem ipsum dolor sit amet, conse ctetur adipiscing elit, sed do eiusmod tempor incididunt ut labore</p>
</div>
<div class="abs service" style="left:450px;top:2441px">
  <svg width="90" height="90" viewBox="0 0 90 90" fill="none" stroke="var(--blue)" stroke-width="2.5"><rect x="4" y="20" width="52" height="44" rx="3"/><path d="M56 36h18l12 14v14H56"/><circle cx="20" cy="68" r="6"/><circle cx="70" cy="68" r="6"/><path d="M20 42l8 8 16-16" stroke="var(--green)"/></svg>
  <h3>Transportation</h3>
  <p class="serif">Lorem ipsum dolor sit amet, conse ctetur adipiscing elit, sed do eiusmod tempor incididunt ut labore</p>
</div>
<div class="abs service" style="left:770px;top:2441px">
  <svg width="90" height="90" viewBox="0 0 90 90" fill="none" stroke="var(--blue)" stroke-width="2.5"><rect x="10" y="24" width="38" height="60"/><path d="M20 24v-8a9 9 0 0 1 18 0v8"/><rect x="40" y="46" width="40" height="38" stroke="var(--green)"/><path d="M52 58v10a8 8 0 0 0 16 0V58" stroke="var(--green)"/></svg>
  <h3>Shopping &amp; Errands</h3>
  <p class="serif">Lorem ipsum dolor sit amet, conse ctetur adipiscing elit, sed do eiusmod tempor incididunt ut labore</p>
</div>
<div class="abs service" style="left:130px;top:2768px">
  <svg width="90" height="90" viewBox="0 0 90 90" fill="none" stroke="var(--blue)" stroke-width="2.5"><path d="M30 6v50"/><path d="M18 56h24l6 26H12z"/><rect x="52" y="46" width="26" height="36" rx="4" stroke="var(--green)"/><path d="M58 46v-8h14v8" stroke="var(--green)"/><path d="M6 30l4 4M10 30l-4 4" stroke="var(--green)"/></svg>
  <h3>Light Housekeeping</h3>
  <p class="serif">Lorem ipsum dolor sit amet, conse ctetur adipiscing elit, sed do eiusmod tempor incididunt ut labore</p>
</div>
<div class="abs service" style="left:450px;top:2768px">
  <svg width="90" height="90" viewBox="0 0 90 90" fill="none" stroke="var(--blue)" stroke-width="2.5"><circle cx="28" cy="12" r="7"/><path d="M20 24h16v30H20zM22 54v30M34 54v30"/><circle cx="58" cy="70" r="14" stroke="var(--green)"/><circle cx="58" cy="36" r="6" stroke="var(--green)"/><path d="M52 44h12v16H48" stroke="var(--green)"/></svg>
  <h3>Stimulating Activities</h3>
  <p class="serif">Lorem ipsum dolor sit amet, conse ctetur adipiscing elit, sed do eiusmod tempor incididunt ut labore</p>
</div>
<div class="abs service" style="left:770px;top:2768px">
  <svg width="90" height="90" viewBox="0 0 90 90" fill="none" stroke="var(--blue)" stroke-width="2.5"><rect x="6" y="20" width="78" height="62" rx="10"/><path d="M32 20v-8h26v8"/><path d="M38 36h14v12h12v14H52v12H38V62H26V48h12z" stroke="var(--green)"/></svg>
  <h3>Medication Reminders</h3>
  <p class="serif">Lorem ipsum dolor sit amet, conse ctetur adipiscing elit, sed do eiusmod tempor incididunt ut labore</p>
</div>
<div class="abs btn services-btn">VIEW OUR SERVICES</div>

<!-- blog -->
<h2 class="abs section-title" style="left:149px;top:3350px">LATEST <span class="b">BLOG</span></h2>
<div class="abs underline" style="left:149px;top:3416px"></div>

<article class="blog-card">
  <div class="abs thumb" style="left:149px;top:3467px;background:linear-gradient(120deg,#c98d61,#e3c7a8 50%,#9a6a45)" role="img" aria-label="Photo of a caregiver laughing with an elderly man"></div>
  <h3 class="abs" style="left:410px;top:3477px">Lorem ipsum dolor sit amet cons ect etur adipiscing</h3>
  <p class="abs serif" style="left:410px;top:3555px">Lorem ipsum dolor sit am etconsectetur adipiscig elit sed do eiusmod tem por incididunt ut lablorore et dolore magna aliqua.</p>
  <div class="abs date" style="left:415px;top:3641px">MAR 19 2022</div>
</article>
<article class="blog-card">
  <div class="abs thumb" style="left:629px;top:3467px;background:linear-gradient(120deg,#9fbfd8,#d9d8cf 50%,#8ca06e)" role="img" aria-label="Photo of a caregiver walking outdoors with a senior woman"></div>
  <h3 class="abs" style="left:890px;top:3477px">Lorem ipsum dolor sit amet cons ect etur adipiscing</h3>
  <p class="abs serif" style="left:890px;top:3555px">Lorem ipsum dolor sit am etconsectetur adipiscig elit sed do eiusmod tem por incididunt ut lablorore et dolore magna aliqua.</p>
  <div class="abs date" style="left:894px;top:3641px">MAR 19 2022</div>
</article>

<!-- contact -->
<div class="abs contact-bg" role="img" aria-label="Background photo of a caregiver with a senior, tinted in teal and green"></div>
<h2 class="abs contact-title">CONTACT US</h2>
<p class="abs contact-sub">The Best Home Care Starts Here</p>

<div class="abs c-item" style="left:267px;top:4025px">
  <div class="dot"><svg width="18" height="18" viewBox="0 0 24 24"><path d="M6.6 10.8a15 15 0 0 0 6.6 6.6l2.2-2.2c.3-.3.7-.4 1-.2 1.1.4 2.3.6 3.6.6.6 0 1 .4 1 1V20c0 .6-.4 1-1 1A17 17 0 0 1 3 4c0-.6.4-1 1-1h3.5c.6 0 1 .4 1 1 0 1.3.2 2.5.6 3.6.1.3 0 .7-.2 1z" fill="var(--blue)"/></svg></div>
  <div>Call us:<br>555 610 4420</div>
</div>
<div class="abs c-item" style="left:480px;top:4025px">
  <div class="dot"><svg width="16" height="20" viewBox="0 0 16 22"><path d="M8 0a8 8 0 0 0-8 8c0 6 8 14 8 14s8-8 8-14a8 8 0 0 0-8-8zm0 11a3 3 0 1 1 0-6 3 3 0 0 1 0 6z" fill="var(--blue)"/></svg></div>
  <div>Address:<br>Location name 12 Elm</div>
</div>
<div class="abs c-item" style="left:733px;top:4025px">
  <div class="dot"><svg width="18" height="14" viewBox="0 0 20 14"><rect width="20" height="14" rx="2" fill="var(--blue)"/><path d="M1 1l9 7 9-7" stroke="#fff" stroke-width="1.6" fill="none"/></svg></div>
  <div>Email:<br>hello@marlowcare.example</div>
</div>

<div class="abs field" style="left:250px;top:4111px;width:342px;height:54px">Name</div>
<div class="abs field" style="left:606px;top:4111px;width:343px;height:54px">Email</div>
<div class="abs field" style="left:250px;top:4181px;width:342px;height:52px">Phone</div>
<div class="abs field" style="left:606px;top:4181px;width:343px;height:52px">Subject</div>
<div class="abs field" style="left:250px;top:4250px;width:699px;height:132px">Message</div>
<div class="abs btn submit">SUBMIT</div>

<svg class="abs" style="left:0;top:4500px" width="1200" height="80" viewBox="0 0 1200 80">
  <path d="M0 72 Q600 -20 1200 72 V80 H0Z" fill="#fff"/>
  <path d="M110 60 Q600 -10 1090 60 Q600 6 110 60Z" fill="var(--blue)"/>
</svg>

<!-- footer -->
<div class="abs footer-brand">
  <div class="mark"></div>
  <div class="name">MARLOW</div>
</div>
<div class="abs f-head" style="left:387px;top:4604px">ABOUT</div>
<p class="abs f-text serif" style="left:387px;top:4636px;width:200px">Lorem ipsum dolor sit am tconsec tetur adipiscig elit sed do eiusmod tem por incididunt ut lablorore et dolore Lorem ipsum dolorsit am etconsectetur adipiscig elit sed do eiusmod teincididunt .</p>
<div class="abs social" style="left:389px;top:4750px"></div>
<div class="abs social" style="left:445px;top:4750px"></div>
<div class="abs social" style="left:502px;top:4750px"></div>

<div class="abs f-head" style="left:663px;top:4604px">LINKS</div>
<div class="abs f-links serif" style="left:663px;top:4634px">Home<br>About<br>Services<br>FAQ<br>Resources<br>Employment<br>Contact</div>

<div class="abs f-head" style="left:808px;top:4604px">NEWSLETTER</div>
<p class="abs f-text serif" style="left:808px;top:4636px;width:250px">Lorem ipsum dolor sit am etconsectetur adipiscig elit sed do eiusmod tem por incididunt ut lablorore et dolore</p>
<div class="abs f-input">Email:</div>
<div class="abs btn f-submit">SUBMIT</div>

<div class="abs divider"></div>
<p class="abs copyright serif">Copyrights © 2022 All Rights Reserved</p>

</body>
</html>
```